Introduction of new dentist and new treatments

We want inform our Patients of our new dentist and new treatment methods. It is dealing about biologic dentistry and holistic dentistry. we are in switzerland and speak german

Font styles to use
Sans Serif

Colors
00a990
33b8a4
9bcb3c
acd036
cadf82
0292cd
3176b5
e34297
e667a6

Requirements
Must have
• Text, which can be edited. It will be in german
• Name of the dental clinic is
• "Brivana - Ihr Zahnarzt in Zug"
Nice to have
• A4 Layout

```html
<!DOCTYPE html>
<html lang="de">
<head>
<meta charset="utf-8">
<title>Brivana – Interdisziplinäre Zahnmedizin</title>
<link rel="stylesheet" href="https://fonts.googleapis.com/css2?family=Lato:wght@400;700&family=Roboto+Slab:wght@500;600&display=swap">
<style>
  :root {
    --page-bg: #a6a6a6;
    --paper: #ffffff;
    --brand-blue: #1273bf;
    --brand-green: #44b04a;
    --heading-blue: #1668b4;
    --navy: #1d2f5c;
    --text: #2b2b2b;
    --photo-light: #e9e4dc;
    --photo-mid: #c9d6d8;
    --portrait-skin: #d9b39b;
    --portrait-shirt: #1f6fc4;
  }
  * { box-sizing: border-box; margin: 0; padding: 0; }
  html, body { width: 1200px; height: 1200px; overflow: hidden; }
  body { background: var(--page-bg); font-family: "Lato", sans-serif; }

  .flyer {
    position: absolute; left: 250px; top: 75px;
    width: 740px; height: 1045px;
    background: var(--paper);
    overflow: hidden;
  }
  .hero-photo {
    position: absolute; left: 0; top: 0; width: 375px; height: 367px;
    background: linear-gradient(135deg, var(--photo-light) 0%, #f3efe9 40%, var(--photo-mid) 100%);
  }
  .brand {
    position: absolute; left: 385px; top: 0; width: 355px; height: 150px;
    text-align: center;
  }
  .brand-name {
    position: absolute; left: 0; right: 0; top: 88px;
    font-size: 27px; font-weight: 400; letter-spacing: 7px;
    color: var(--navy);
  }
  .brand-tagline {
    position: absolute; left: 0; right: 0; top: 123px;
    font-size: 11px; color: var(--navy);
  }
  .intro-box {
    position: absolute; left: 385px; top: 154px; width: 355px; height: 213px;
    background: var(--brand-blue);
    padding: 10px 44px 0 30px;
  }
  .intro-title {
    font-family: "Roboto Slab", serif; font-weight: 600;
    font-size: 17.5px; line-height: 22.5px;
    color: #5fd24f;
  }
  .intro-text {
    margin-top: 10px;
    font-size: 13px; line-height: 20px;
    color: #fff; text-align: justify;
  }
  .rule-green {
    position: absolute; left: 0; width: 740px; height: 9px;
    background: var(--brand-green);
  }
  .rule-top { top: 376px; }
  .rule-bottom { top: 1009px; }
  .footer-band {
    position: absolute; left: 0; top: 1018px; width: 740px; height: 27px;
    background: var(--navy);
  }
  .section { position: absolute; left: 26px; width: 688px; }
  .section-title {
    font-family: "Roboto Slab", serif; font-weight: 500;
    font-size: 18.5px; line-height: 24px;
    text-decoration: underline; text-underline-offset: 3px; text-decoration-thickness: 1px;
  }
  .section-title .lead { color: var(--brand-green); }
  .section-title .tail { color: var(--heading-blue); }
  .section p {
    font-size: 12.6px; line-height: 16.4px;
    color: var(--text); text-align: justify;
    hyphens: auto; -webkit-hyphens: auto;
  }
  .s1 { top: 407px; }
  .s1 p:first-of-type { margin-top: 11px; }
  .s1 p + p { margin-top: 12px; }
  .s2 { top: 578px; }
  .s2 p { margin-top: 20px; }
  .s3 { top: 725px; }
  .s3 p { margin-top: 11px; }
  .s4 { top: 841px; width: 474px; }
  .s4 p { margin-top: 10px; }
  .portrait {
    position: absolute; left: 512px; top: 819px; width: 208px; height: 226px;
    border-radius: 90px 90px 0 0;
    background: linear-gradient(180deg, var(--portrait-skin) 0%, var(--portrait-skin) 62%, var(--portrait-shirt) 78%, var(--portrait-shirt) 100%);
  }
</style>
</head>
<body>
  <main class="flyer">
    <div class="hero-photo" role="img" aria-label="Foto: älterer Patient lächelnd im Behandlungsstuhl einer Zahnarztpraxis"></div>

    <header class="brand">
      <div class="brand-name">BRIVANA</div>
      <div class="brand-tagline">Ihr Zahnarzt in Zug</div>
    </header>

    <section class="intro-box">
      <h1 class="intro-title">Interdisziplinäre Zahnmedizin – Zusammenhang zwischen Zahnproblemen und der Gesundheit von Körper und Geist</h1>
      <p class="intro-text">Zahn und Gesundheit haben eins gemeinsam – Man vermisst sie, wenn sie fehlt. Zähne haben einen engen Zusammenhang zur Gesundheit und können diese beeinflussen. Sowohl negativ als auch positiv.</p>
    </section>

    <div class="rule-green rule-top"></div>

    <section class="section s1">
      <h2 class="section-title"><span class="lead">Funktion des Kauorgans</span><span class="tail"> und interdisziplinäre Zahnmedizin</span></h2>
      <p>Funktion ist nicht alles. Aber ohne Funktion ist alles nichts!“ Sagte einst Prof. A. Lenhardt (Zahnarzt, Gnathologie) und betonte die Bedeutung der Funktion des Kausystems.</p>
      <p>Sprechen, Kauen aber auch Körperhaltung und Stressmanagement gehören zu den Funktionen der Zähne. Ein gut funktionierendes Kauorgan (nach Prof. R. Marovic, interdisziplinäre Zahnmedizin) kann Stress bewältigen und mehr Leistung und Wohlbefinden bringen. Sehr oft erkennt man Funktionsstörungen daran, dass die Zähne nicht richtig zueinander passen oder Muskelverspannungen und Schmerzen im Kiefergelenk auftreten.</p>
    </section>

    <section class="section s2">
      <h2 class="section-title"><span class="lead">Parodontitis und</span><span class="tail"> systemische Erkrankungen</span></h2>
      <p>Parodontitis (Entzündung des Zahnhalteapparats) ist eine der häufigsten chronischen Krankheiten weltweit und daher gut erforscht. Herzkrankheiten, Diabetes und Frühgeburtlichkeit sind einige der systemischen Krankheiten mit der Parodontitis in Zusammenhang steht. Zahnfleischbulten, Zahnlockerung, Zahnfleischschwund und Zahnverlust sind typische Begleiterscheinungen von Parodontitis. Eine systematische Parodontitis-Behandlung kann auch positive Auswirkungen auf die gesamte Gesundheit haben.</p>
    </section>

    <section class="section s3">
      <h2 class="section-title"><span class="lead">Zahnverlust und</span><span class="tail"> neurologische Auswirkung</span></h2>
      <p>Ein physiologisches Kausystem hat sehr feine Steuerungs- und Wahrnehmungsmöglichkeiten. Bei Zahnverlust werden diese Fähigkeiten weniger benötigt. Weniger gebrauchte Ressourcen werden von der Natur dementsprechend abgebaut. Studien zeigen, dass Menschen mit weniger Zähnen mehr Risiko zur Bildung von Demenz bergen.</p>
    </section>

    <section class="section s4">
      <h2 class="section-title"><span class="lead">Ganzheitliche</span><span class="tail"> Erklärungen</span></h2>
      <p>Die komplementäre Zahnheilkunde, sehr oft auch als ganzheitliche oder biologische Zahnheilkunde bezeichnet, versucht mit Hilfe von Meridianen (Traditionelle Chinesische Medizin), den Zusammenhang zwischen Zähnen und anderen Organen und Körperteilen zu erklären. Es gibt immer mehr Patienten und Zahnärzte die von dieser Theorie und deren Ergebnissen überzeugt sind. Aufgrund der wissenschaftlichen Lage ist eine ausführliche Aufklärung vor der Behandlung sehr ratsam.</p>
    </section>

    <div class="rule-green rule-bottom"></div>
    <div class="footer-band"></div>

    <div class="portrait" role="img" aria-label="Porträtfoto des neuen Zahnarztes im blauen Poloshirt"></div>
  </main>
</body>
</html>
```